Modern Catering Company needs Letterhead Design

We need a letterhead design that will make effective use of the corporate logo and color scheme, along with careful typography, helps this letterhead design communicate the brand well. We do have a corporate logo, however feel free to enhance the color scheme with gold and purple. We are serving a very upscale clientele so the letterhead has to reflect elegance, professionalism, cleanliness, and modern style. We are branding the company so the letterhead and business cards must fit the brand story. There should be no cartoonish elements in the design and we are looking for sharper lines.

Target Market(s)

Businesses and upscale clientele

Industry/Entity Type

Catering

Contact Information for Business Card

while this design can have any number of quirks and distinctions, it needs to be cohesive with the entire brand story clean, professional but edgy

Requirements
Must have
• must have good and carefully placement of it’s logo and where you place the text or the message. Colors blue, very deep purple, jewel tones not pastels, gold. Blue must be the primary color you may accent with purple or gold. Contact information is as follows: Co-Owners/ Chefs: R. Hollowell & T. Brenn, phone: 414-555-0182 email:Contact@emberoakcatering.example, address: 6172 W Larkmoor Ln, Milwaukee, WI 53299
Should not have
• pastel colors, Do not add the BBQ information to the letterhead or business card it was a mistake by the previous designer.

```html
<!DOCTYPE html>
<html lang="en">
<head>
<meta charset="utf-8">
<title>Ember Oak Catering – Business Card</title>
<link href="https://fonts.googleapis.com/css2?family=Source+Sans+3:wght@400;600&display=swap" rel="stylesheet">
<style>
  :root {
    --backdrop: #474747;
    --card-white: #ffffff;
    --blue: #1c3f94;
    --blue-deep: #2a2a78;
    --gold: #e9b43a;
    --gold-light: #f8e38c;
    --gold-mid: #f2cf62;
    --gold-deep: #e3aa3c;
    --ink: #4a4a4a;
  }
  html, body {
    margin: 0;
    padding: 0;
    width: 1105px;
    height: 1200px;
    overflow: hidden;
    background: var(--backdrop);
    font-family: "Source Sans 3", sans-serif;
  }
  .canvas { position: relative; width: 1105px; height: 1200px; }

  .card {
    position: absolute;
    left: 196px;
    width: 720px;
    height: 412px;
    box-shadow: 0 4px 10px rgba(0,0,0,0.45);
    overflow: hidden;
  }

  /* Front */
  .card-front { top: 146px; background: var(--card-white); }
  .brand-mark {
    position: absolute;
    left: 70px;
    top: 112px;
    width: 250px;
    text-align: center;
    color: var(--blue);
    font-weight: 600;
    font-size: 40px;
    line-height: 1.1;
    letter-spacing: 3px;
  }
  .brand-mark .brand-dot {
    display: block;
    width: 16px; height: 16px;
    border-radius: 50%;
    background: var(--blue);
    margin: 0 auto 16px;
  }
  .contact-block {
    position: absolute;
    left: 350px;
    top: 84px;
    color: var(--ink);
  }
  .person-name { margin: 0; font-size: 25px; font-weight: 600; color: var(--gold); line-height: 1.1; }
  .person-role { margin: 4px 0 18px; font-size: 19px; color: var(--blue); }
  .address { margin: 0 0 10px; font-size: 18px; line-height: 1.3; }
  .contact-line { display: flex; align-items: center; gap: 9px; font-size: 18.5px; line-height: 1.6; }
  .contact-line svg { width: 16px; height: 16px; flex: none; }
  .rule-blue { position: absolute; left: 0; right: 0; top: 379px; height: 3px; background: var(--blue-deep); }
  .band-gold {
    position: absolute; left: 0; right: 0; top: 383px; bottom: 0;
    background: linear-gradient(90deg, var(--gold-deep), var(--gold-light) 50%, var(--gold-deep));
  }

  /* Back */
  .card-back {
    top: 602px;
    background: radial-gradient(ellipse at 50% 42%, var(--gold-light) 0%, var(--gold-mid) 40%, var(--gold-deep) 100%);
  }
  .back-brand {
    position: absolute; left: 0; right: 0; top: 170px;
    margin: 0;
    text-align: center; color: var(--blue);
    font-size: 38px; font-weight: 600; letter-spacing: 3px; line-height: 1.1;
  }
  .back-web {
    position: absolute; left: 0; right: 0; top: 358px; margin: 0;
    text-align: center; font-size: 19px; letter-spacing: 1.5px; color: var(--ink);
  }
</style>
</head>
<body>
<main class="canvas">
  <section class="card card-front" aria-label="Business card front">
    <div class="brand-mark"><span class="brand-dot"></span>EMBER OAK<br>CATERING</div>
    <div class="contact-block">
      <h1 class="person-name">R. Hollowell &amp; T. Brenn</h1>
      <p class="person-role">Co-Owners / Chefs</p>
      <p class="address">6172 W Larkmoor Ln<br>Milwaukee, WI 53299</p>
      <div class="contact-line">
        <svg viewBox="0 0 16 16" aria-hidden="true"><path fill="#e9b43a" d="M3.5 1.5l2.5 0 1.2 3.2-1.6 1.2c.8 1.7 2 2.9 3.7 3.7l1.2-1.6 3.2 1.2v2.5c0 .8-.7 1.5-1.5 1.5C6.6 13.2 2.8 9.4 2 3c0-.8.7-1.5 1.5-1.5z"/></svg>
        <span>414-555-0182</span>
      </div>
      <div class="contact-line">
        <svg viewBox="0 0 16 16" aria-hidden="true"><rect x="1" y="3" width="14" height="10" rx="1" fill="#e9b43a"/><path d="M1.5 3.8L8 9l6.5-5.2" fill="none" stroke="#fff" stroke-width="1.3"/></svg>
        <span>Contact@emberoakcatering.example</span>
      </div>
      <div class="contact-line">
        <svg viewBox="0 0 16 16" aria-hidden="true"><circle cx="8" cy="8" r="7" fill="#e9b43a"/><path d="M1 8h14M8 1c-2.5 3-2.5 11 0 14M8 1c2.5 3 2.5 11 0 14" fill="none" stroke="#fff" stroke-width="1"/></svg>
        <span>www.emberoakcatering.example</span>
      </div>
    </div>
    <div class="rule-blue"></div>
    <div class="band-gold"></div>
  </section>

  <section class="card card-back" aria-label="Business card back">
    <h2 class="back-brand">EMBER OAK<br>CATERING</h2>
    <p class="back-web">www.emberoakcatering.example</p>
  </section>
</main>
</body>
</html>
```